Team email banner for internal communications

We need a team email banner/header that will be applied to all internal communications from our department to other functions. The graphic should be optimized for Outlook and be landscape in layout. We have 5 different silo within our team and will need so will either need have a blank space to denote each team or have change in colors/graphics to denote each team (see current headers attached to job description). We are looking for a banner that combines our team logo (attached) with our team name, Regional Talent & Coaching Unit. The theme should be L&D and pharmaceutical in nature.

Need extra days to review

The text in the banner should be Regional Talent & Coaching Unit with the team logo (attached).

```html
<!DOCTYPE html>
<html lang="en">
<head>
<meta charset="utf-8">
<title>Regional Talent &amp; Coaching Unit – Team Email Banners</title>
<link rel="stylesheet" href="https://fonts.googleapis.com/css2?family=Montserrat:ital,wght@0,800;1,700;1,800&display=swap">
<style>
  :root {
    --page-bg: #e8e8e8;
    --white: #ffffff;
    --ink: #121212;
    --accent-red: #d8261c;
    --hematology: #bb1b12;
    --solid-tumor: #520a43;
    --leadership: #252a37;
  }
  * { margin: 0; padding: 0; box-sizing: border-box; }
  html, body {
    width: 1043px; height: 1200px; overflow: hidden;
    background: var(--page-bg);
    font-family: "Montserrat", Arial, sans-serif;
  }
  .banner {
    position: absolute; left: 33px;
    width: 977px; height: 326px;
    background: var(--team-colour);
    overflow: hidden;
  }
  .banner--hematology { top: 62px; --team-colour: var(--hematology); }
  .banner--solid-tumor { top: 434px; --team-colour: var(--solid-tumor); }
  .banner--leadership { top: 811px; --team-colour: var(--leadership); }

  .banner__art { position: absolute; inset: 0; width: 977px; height: 326px; }

  .team-mark {
    position: absolute; left: 41px; top: 0;
    width: 108px; height: 131px;
    background: var(--white);
    border-radius: 0 0 6px 6px;
    display: flex; flex-direction: column; align-items: center; justify-content: center; gap: 10px;
  }
  .team-mark__dot { width: 30px; height: 30px; border-radius: 50%; background: var(--accent-red); }
  .team-mark__name { font-weight: 800; font-size: 24px; color: var(--ink); letter-spacing: 0.5px; }

  .team-name {
    position: absolute; left: 33px; top: 142px;
    color: var(--white);
    font-weight: 800; font-style: italic;
    font-size: 41px; line-height: 44px;
    letter-spacing: 0.3px;
  }
  .silo-tag {
    position: absolute; left: 0; top: 240px; height: 57px;
    background: var(--white);
    border-radius: 0 12px 12px 0;
    padding: 0 28px 0 27px;
    display: flex; align-items: center;
    color: var(--team-colour);
    font-weight: 800; font-style: italic; font-size: 38px;
    white-space: nowrap;
  }
</style>
</head>
<body>

<section class="banner banner--hematology">
  <svg class="banner__art" viewBox="0 0 977 326">
    <defs>
      <linearGradient id="photo-hematology" x1="0" y1="0" x2="1" y2="1">
        <stop offset="0" stop-color="#3d5e70"/><stop offset="0.35" stop-color="#8fc9cf"/>
        <stop offset="0.6" stop-color="#a3161a"/><stop offset="1" stop-color="#5b1218"/>
      </linearGradient>
    </defs>
    <path role="img" aria-label="Close-up of red blood cells floating in blue fluid" fill="url(#photo-hematology)"
      d="M574 0 H977 V326 H621 V200 Q621 176 600 165 Q574 150 574 120 Z"/>
  </svg>
  <div class="team-mark"><span class="team-mark__dot"></span><span class="team-mark__name">RTCU</span></div>
  <h1 class="team-name">Regional Talent<br>&amp; Coaching Unit</h1>
  <p class="silo-tag">Hematology</p>
</section>

<section class="banner banner--solid-tumor">
  <svg class="banner__art" viewBox="0 0 977 326">
    <defs>
      <linearGradient id="photo-solid-tumor" x1="0" y1="0" x2="1" y2="1">
        <stop offset="0" stop-color="#1b2fa0"/><stop offset="0.4" stop-color="#6a8de0"/>
        <stop offset="0.6" stop-color="#b25ad8"/><stop offset="1" stop-color="#4a0e6a"/>
      </linearGradient>
    </defs>
    <path role="img" aria-label="3D rendering of a textured tumour cell in blue and violet" fill="url(#photo-solid-tumor)"
      d="M574 0 H977 V326 H621 V200 Q621 176 600 165 Q574 150 574 120 Z"/>
  </svg>
  <div class="team-mark"><span class="team-mark__dot"></span><span class="team-mark__name">RTCU</span></div>
  <h1 class="team-name">Regional Talent<br>&amp; Coaching Unit</h1>
  <p class="silo-tag">Solid Tumor</p>
</section>

<section class="banner banner--leadership">
  <svg class="banner__art" viewBox="0 0 977 326">
    <defs>
      <linearGradient id="photo-leadership" x1="0" y1="0" x2="1" y2="1">
        <stop offset="0" stop-color="#c5c8cb"/><stop offset="0.35" stop-color="#3b4150"/>
        <stop offset="0.7" stop-color="#2a2c31"/><stop offset="1" stop-color="#c9b9a3"/>
      </linearGradient>
    </defs>
    <path role="img" aria-label="Businessman behind chess pieces on a wooden board" fill="url(#photo-leadership)"
      d="M574 0 H977 V326 H621 V200 Q621 176 600 165 Q574 150 574 120 Z"/>
  </svg>
  <div class="team-mark"><span class="team-mark__dot"></span><span class="team-mark__name">RTCU</span></div>
  <h1 class="team-name">Regional Talent<br>&amp; Coaching Unit</h1>
  <p class="silo-tag">Leadership Development</p>
</section>

</body>
</html>
```